Classic/Royal 5 Items Black coloured Stationery Design

Hello,
I'm looking for an Elegant Stationery set consists of 5 items as the following,
1- Letterhead
2- Business Card
3- Invoice
4- CD/DVD with their Envelope Design
5- Envelope
To let the project move ahead easily, I've included a folder consists many designs I liked from various design sites and it consists of,
1- Business card
2- Corporate Identity
3- Invoice
4- Miscellanies
Inside the first three folders, you will find a folder named "Recommended", it contains designs that I like so much and hoping to have a design like them.
The "Miscellanies" folder got some designs for Inspiration.
I'm waiting for some greats designs, a joomla template designer is a bonus for me as I will need him to design the website layer soon.
Due to upload problems at ArtHerdly, I've uploaded the folder in a .rar archive at multiple site and here is the link http://zup.qx/TRALVBNE .
Thank you
Update :- You can use this alternative download link from my Google drive to download the designs
https://files.plomwex.net/file/d/7Kq2ZpR4m8sVxT1nLw9cYb3HfJd5

```html
<!DOCTYPE html>
<html lang="en">
<head>
<meta charset="utf-8">
<title>Velmora Stationery Set</title>
<link rel="stylesheet" href="https://fonts.googleapis.com/css2?family=Bodoni+Moda:wght@400;500&family=Questrial&display=swap">
<style>
  :root {
    --bg: #eeeeee;
    --paper: #ffffff;
    --ink-dark: #1d1d1d;
    --pattern-top: #2c2c2c;
    --pattern-bottom: #161616;
    --brand-grey: #8e8e8e;
    --brand-light: #c9c9c9;
    --rule-grey: #b5b5b5;
    --text-dark: #222222;
    --window: #f4f4f4;
  }
  * { box-sizing: border-box; margin: 0; padding: 0; }
  html, body { width: 1200px; height: 926px; overflow: hidden; }
  body { background: var(--bg); position: relative; font-family: "Questrial", sans-serif; }

  .piece { position: absolute; }
  .damask {
    background: linear-gradient(180deg, var(--pattern-top), var(--pattern-bottom));
  }

  /* brand block */
  .brand { position: absolute; display: flex; flex-direction: column; align-items: center; text-align: center; }
  .brand-mark { background: var(--ink-dark); border: 2px solid var(--brand-light); }
  .brand-name { font-family: "Bodoni Moda", serif; font-weight: 500; color: var(--brand-grey); line-height: 1; }
  .brand-tagline { font-family: "Questrial", sans-serif; color: var(--brand-grey); white-space: nowrap; }
  .on-dark .brand-name, .on-dark .brand-tagline { color: var(--brand-light); }

  /* letterhead */
  .letterhead { left: 38px; top: 70px; width: 529px; height: 788px; background: var(--paper); }
  .letterhead .brand { left: 0; right: 0; top: 38px; }
  .letterhead .brand-mark { width: 46px; height: 60px; }
  .letterhead .brand-name { font-size: 25px; margin-top: 6px; }
  .letterhead .brand-tagline { font-size: 10.5px; margin-top: 4px; }
  .letterhead-contact {
    position: absolute; left: 0; right: 0; top: 716px; display: flex; justify-content: space-between;
    padding: 0 96px; font-family: "Bodoni Moda", serif; font-size: 10px; color: var(--text-dark);
  }
  .letterhead-rule { position: absolute; left: 0; right: 0; top: 733px; height: 7px; background: var(--rule-grey); }
  .letterhead-band { position: absolute; left: 0; right: 0; bottom: 0; height: 48px; }

  /* business cards */
  .card { width: 221px; height: 131px; }
  .card-front { left: 633px; top: 87px; }
  .card-back { left: 633px; top: 237px; height: 132px; width: 223px; }
  .card .brand { left: 0; right: 0; }
  .card-front .brand { top: 37px; }
  .card-back .brand { top: 15px; }
  .card .brand-mark { width: 25px; height: 32px; }
  .card .brand-name { font-size: 14px; margin-top: 3px; }
  .card .brand-tagline { font-size: 6.5px; margin-top: 2px; }
  .card-person {
    position: absolute; left: 0; right: 0; top: 77px; text-align: center;
    font-family: "Bodoni Moda", serif; font-size: 7.5px; letter-spacing: 1.5px; color: var(--brand-light);
  }
  .card-details {
    position: absolute; left: 0; right: 0; top: 97px; text-align: center;
    font-family: "Bodoni Moda", serif; font-size: 5.5px; line-height: 9px; color: var(--brand-light);
  }

  /* envelope */
  .envelope { left: 430px; top: 404px; width: 460px; height: 323px; }
  .envelope-flap { position: absolute; left: 0; top: 0; width: 460px; height: 70px; }
  .envelope-body { position: absolute; left: 0; top: 68px; width: 460px; height: 238px; background: var(--paper); }
  .envelope-band { position: absolute; left: 0; bottom: 0; width: 460px; height: 17px; }
  .envelope .brand { left: 47px; top: 30px; width: 124px; }
  .envelope .brand-mark { width: 38px; height: 50px; }
  .envelope .brand-name { font-size: 20px; margin-top: 4px; }
  .envelope .brand-tagline { font-size: 8.5px; margin-top: 3px; }
  .envelope-window {
    position: absolute; left: 48px; top: 142px; width: 174px; height: 74px;
    background: var(--window); border: 1px solid #dddddd; border-radius: 10px;
  }

  /* disc and sleeve */
  .disc { left: 890px; top: 407px; width: 268px; height: 268px; }
  .disc .brand { left: 0; right: 0; top: 33px; }
  .disc .brand-mark { width: 28px; height: 37px; }
  .disc .brand-name { font-size: 15px; margin-top: 4px; }
  .disc .brand-tagline { font-size: 7px; margin-top: 2px; }
  .sleeve { left: 878px; top: 558px; width: 287px; height: 285px; background: var(--paper); }
  .sleeve-cover { position: absolute; left: 0; top: 0; width: 287px; height: 210px; }
  .sleeve .brand { left: 0; right: 0; top: 81px; }
  .sleeve .brand-mark { width: 42px; height: 55px; }
  .sleeve .brand-name { font-size: 22px; margin-top: 5px; }
  .sleeve .brand-tagline { font-size: 9.5px; margin-top: 3px; }
  .sleeve-title {
    position: absolute; left: 0; right: 0; top: 229px; text-align: center;
    font-family: "Bodoni Moda", serif; font-size: 17px; color: var(--text-dark);
  }
  .sleeve-subtitle {
    position: absolute; left: 0; right: 0; top: 251px; text-align: center;
    font-size: 12px; color: var(--text-dark);
  }
</style>
</head>
<body>

<section class="piece letterhead">
  <div class="brand">
    <div class="brand-mark"></div>
    <div class="brand-name">Velmora</div>
    <div class="brand-tagline">Hotels and General Supplies</div>
  </div>
  <div class="letterhead-contact">
    <span>(555) 218 4096</span>
    <span>danielcrane@velmora.com</span>
    <span>www.velmora.com</span>
  </div>
  <div class="letterhead-rule"></div>
  <div class="letterhead-band damask" role="img" aria-label="Dark damask pattern band"></div>
</section>

<section class="piece card card-front damask on-dark" role="img" aria-label="Business card front with dark damask pattern">
  <div class="brand">
    <div class="brand-mark"></div>
    <div class="brand-name">Velmora</div>
    <div class="brand-tagline">Hotels and General Supplies</div>
  </div>
</section>

<section class="piece card card-back damask on-dark" role="img" aria-label="Business card back with dark damask pattern">
  <div class="brand">
    <div class="brand-mark"></div>
    <div class="brand-name">Velmora</div>
    <div class="brand-tagline">Hotels and General Supplies</div>
  </div>
  <div class="card-person">DANIEL R. CRANE</div>
  <div class="card-details">(555) 218 4096<br>danielcrane@velmora.com<br>www.velmora.com</div>
</section>

<section class="piece envelope">
  <svg class="envelope-flap" viewBox="0 0 460 70" role="img" aria-label="Envelope flap with dark damask pattern">
    <defs>
      <linearGradient id="flapShade" x1="0" y1="0" x2="0" y2="1">
        <stop offset="0" stop-color="#2c2c2c"/>
        <stop offset="1" stop-color="#1a1a1a"/>
      </linearGradient>
    </defs>
    <path d="M0 70 L14 8 Q16 0 26 0 L434 0 Q444 0 446 8 L460 70 Z" fill="url(#flapShade)"/>
  </svg>
  <div class="envelope-body">
    <div class="brand">
      <div class="brand-mark"></div>
      <div class="brand-name">Velmora</div>
      <div class="brand-tagline">Hotels and General Supplies</div>
    </div>
    <div class="envelope-window"></div>
  </div>
  <div class="envelope-band damask" role="img" aria-label="Dark damask pattern band"></div>
</section>

<section class="piece disc on-dark">
  <svg viewBox="0 0 268 268" width="268" height="268" style="position:absolute;left:0;top:0" role="img" aria-label="Disc label with dark damask pattern">
    <defs>
      <linearGradient id="discShade" x1="0" y1="0" x2="0" y2="1">
        <stop offset="0" stop-color="#2e2e2e"/>
        <stop offset="1" stop-color="#161616"/>
      </linearGradient>
    </defs>
    <circle cx="134" cy="134" r="134" fill="url(#discShade)"/>
    <circle cx="134" cy="134" r="128" fill="none" stroke="#ffffff" stroke-width="2"/>
    <circle cx="134" cy="134" r="16" fill="#ffffff"/>
  </svg>
  <div class="brand">
    <div class="brand-mark"></div>
    <div class="brand-name">Velmora</div>
    <div class="brand-tagline">Hotels and General Supplies</div>
  </div>
</section>

<section class="piece sleeve">
  <div class="sleeve-cover damask on-dark" role="img" aria-label="Disc sleeve cover with dark damask pattern">
    <div class="brand">
      <div class="brand-mark"></div>
      <div class="brand-name">Velmora</div>
      <div class="brand-tagline">Hotels and General Supplies</div>
    </div>
  </div>
  <div class="sleeve-title">Your Title Here</div>
  <div class="sleeve-subtitle">Subtitle Here</div>
</section>

</body>
</html>
```